improvement on my landing page

We are a fansite platform similar to brindlefold.com, quillmarsh.com , tovarenel.com and gleamwick.com. We are aiming to disrupt this space by a much cheaper and advanced platform to help influencers monetise across different tools.

current lander is https://lumorabey.com/

Looking for a modern, clean, feminine , pink. Current style and other competitors list given feel old and this needs to highlight its a cutting edge product replacing them. Designs I like are www.kelvadrop.app for example.

I need a few elaborations from current site on price differences of competitors, icons and more details on features and several other new sections added. Need a form to capture email , name and phone as this is a coming soon page. Can change later as a signup

attached document is how thee site looks, so need to keep the identity

Target Market(s)

influence's, adult

Font styles to use
Sans Serif

Colors
eea4c8
fefafc
ecdaeb

Requirements
Nice to have
• infographics

```html
<!DOCTYPE html>
<html lang="en">
<head>
<meta charset="utf-8">
<title>Lumorabey — Keep 90% of your earnings</title>
<link href="https://fonts.googleapis.com/css2?family=Jost:wght@400;500;600&display=swap" rel="stylesheet">
<style>
:root{
  --pink:#e0408f;
  --pink-hot:#e53b8c;
  --pink-soft:#eea4c8;
  --blush:#fbe6f5;
  --paper:#ffffff;
  --ink:#2f2f35;
  --lilac-light:#ede0f9;
  --lilac:#c2a7ee;
  --sky:#00c3f8;
  --blue:#005fe8;
  --field:#ffffff;
  --muted:#9a9aa5;
}
*{box-sizing:border-box;margin:0;padding:0}
html,body{width:672px;height:1200px;overflow:hidden;background:var(--paper)}
body{font-family:'Jost',sans-serif;color:var(--ink);position:relative}
.abs{position:absolute}

/* hero */
.hero{left:0;top:0;width:672px;height:278px;overflow:hidden}
.hero-photo{position:absolute;inset:0;background:
  radial-gradient(ellipse 90px 120px at 350px 150px,#d9b4a8 0%,rgba(217,180,168,0) 100%),
  linear-gradient(90deg,#3b3a2e 0%,#6b5644 35%,#8a7260 55%,#6f5a48 80%,#4e463a 100%)}
.hero-shade{position:absolute;inset:0;background:linear-gradient(90deg,rgba(0,0,0,.35),rgba(0,0,0,0) 60%)}
.brand{left:41px;top:24px;font-size:29px;font-weight:500;letter-spacing:2px;color:#fff}
.hero-title{left:41px;top:112px;text-align:center;white-space:nowrap;font-size:16px;font-weight:500;letter-spacing:1.1px;color:#fff;line-height:25px}
.hero-sub{left:41px;top:181px;width:220px;text-align:center;font-size:7.6px;color:#fff;line-height:12.6px}
.hero-sub b{color:var(--pink-soft);font-weight:600}
.btn{display:flex;align-items:center;justify-content:center;border-radius:12px;font-size:7.5px;font-weight:600;color:#fff}
.btn-primary{background:var(--pink)}
.btn-ghost{border:1px solid #fff;font-weight:500}

/* why */
.why-brand{left:0;width:672px;top:313px;text-align:center;font-size:29px;font-weight:500;letter-spacing:2px;color:var(--ink)}
.why-title{left:0;width:672px;top:362px;text-align:center;font-size:12.5px;font-weight:500;letter-spacing:1.3px}
.why-title span{color:var(--pink)}
.art{border-radius:14px}
.copy{font-size:7.2px;line-height:11.3px;letter-spacing:.3px;font-weight:500}
.copy em{font-style:normal;color:var(--pink);font-weight:600}

/* features */
.features{left:0;top:708px;width:672px;height:231px;background:linear-gradient(180deg,var(--sky),var(--blue))}
.feature{position:absolute;top:78px;width:130px;margin-left:-65px;text-align:center;color:#fff}
.feature svg{display:block;margin:0 auto 4px}
.feature h3{font-size:7.6px;font-weight:600;letter-spacing:.2px;padding-bottom:2px;border-bottom:1px solid rgba(255,255,255,.35);display:inline-block}
.feature p{font-size:6.8px;line-height:10px;color:rgba(255,255,255,.85);margin-top:2px}
.arrow{position:absolute;top:106px}

/* fees */
.fees{left:72px;top:973px;width:327px;height:159px;background:var(--lilac-light);overflow:hidden}
.fees-label{font-size:10px;font-weight:600;letter-spacing:.3px}
.rival{position:absolute;left:26px;display:flex;align-items:center;gap:6px;font-size:7px;font-weight:600;color:#55525e}
.rival i{width:12px;height:12px;border-radius:50%;display:block}
.rate{position:absolute;left:98px;font-size:10px;font-weight:600;color:#6f6b78}
.our{position:absolute;left:190px;width:120px;text-align:center;color:#fff}

/* form */
.signup-title{left:456px;width:146px;top:969px;text-align:center;font-size:10.6px;font-weight:600}
.signup{left:466px;top:999px;width:131px;height:133px;background:var(--blush);border-radius:4px}
.field{position:absolute;left:12px;width:106px;height:15px;background:var(--field);border:1px solid #f2dcea;border-radius:4px;font-size:5.6px;color:var(--muted);padding-left:8px;display:flex;align-items:center}

.footer{left:0;top:1158px;width:672px;height:42px;background:var(--pink-hot);color:#fff;font-size:7px;font-weight:500;display:flex;align-items:center;justify-content:center}
</style>
</head>
<body>

<header class="abs hero">
  <div class="hero-photo" role="img" aria-label="Photo of a smiling woman on a sofa working on a laptop in a warm café"></div>
  <div class="hero-shade"></div>
  <div class="abs brand">LUMORABEY</div>
  <h1 class="abs hero-title">KEEP 90% OF YOUR EARNINGS<br>NO HIDDEN FEES.</h1>
  <p class="abs hero-sub">Make more with added revenue streams and features for <b>FREE</b>.<br>Maximise you're your fanbase profits with Lumorabey.</p>
  <a class="abs btn btn-primary" style="left:42px;top:224px;width:101px;height:23px">GET STARTED</a>
  <a class="abs btn btn-ghost" style="left:148px;top:224px;width:102px;height:23px">Learn More</a>
</header>

<section>
  <h2 class="abs why-brand">LUMORABEY</h2>
  <h3 class="abs why-title">WHY CHOOSE <span>US</span>?</h3>

  <div class="abs art" style="left:58px;top:396px;width:154px;height:133px;background:linear-gradient(160deg,#dcecf6,#f5f9fc 70%)" role="img" aria-label="Illustration of a woman working at a laptop desk with like and heart bubbles"></div>
  <p class="abs copy" style="left:227px;top:444px;width:336px">Lumorabey was developed to democratise the fan platform space.As entrepreneurs ourselves we don't see why you should you be handing over a high percentageof your hard earned profits to platforms with mediocre features and services. <em>RECEIVE 90%</em> of your earnings, with no hidden fees or extrasAND with fastest payouts.</p>

  <p class="abs copy" style="left:161px;top:574px;width:247px">Monetize with monthly subscriptions through private profile feeds and premium social media accounts. Private messaging and tipping, premium videos and much more.<br><em>START EARNING MORE AND KEEPING YOUR PROFITS</em>.</p>
  <div class="abs art" style="left:418px;top:524px;width:201px;height:133px;background:linear-gradient(160deg,#eef6f4,#f8f4fb)" role="img" aria-label="Illustration of two people leaping out of phones surrounded by chat and gift icons"></div>
  <div class="abs" style="left:418px;top:657px;width:201px;height:1px;background:#e3dcf5"></div>
</section>

<section class="abs features">
  <svg class="arrow" style="left:71px" width="12" height="20" viewBox="0 0 12 20"><path d="M10 1 2 10l8 9" fill="none" stroke="#fff" stroke-width="1.4"/></svg>
  <svg class="arrow" style="left:586px" width="12" height="20" viewBox="0 0 12 20"><path d="m2 1 8 9-8 9" fill="none" stroke="#fff" stroke-width="1.4"/></svg>

  <div class="feature" style="left:163px">
    <svg width="34" height="34" viewBox="0 0 34 34" fill="none" stroke="#fff" stroke-width="1.3"><path d="M4 3h16M4 31h16M6 3c0 9 10 9 10 14S6 22 6 31M18 3c0 9-10 9-10 14s10 5 10 14"/><circle cx="26" cy="18" r="6"/><path d="M26 14v8M24 16h3.5M24.5 20h3"/></svg>
    <h3>FASTEST PAYOUTS</h3>
    <p>Get your money in less<br>than 7 days</p>
  </div>
  <div class="feature" style="left:257px">
    <svg width="34" height="34" viewBox="0 0 34 34" fill="none" stroke="#fff" stroke-width="1.3"><circle cx="15" cy="18" r="11"/><path d="M4 18h22M15 7c-5 6-5 16 0 22M15 7c5 6 5 16 0 22"/><rect x="23" y="24" width="8" height="7" rx="1"/><path d="M25 24v-2a2 2 0 0 1 4 0v2"/></svg>
    <h3>GEO BLOCKING</h3>
    <p>Hide your content from<br>specific countries</p>
  </div>
  <div class="feature" style="left:360px">
    <svg width="34" height="34" viewBox="0 0 34 34" fill="none" stroke="#fff" stroke-width="1.3"><path d="M7 2h15l6 6v24H7z"/><path d="M17 9l8 3v6c0 5-4 8-8 10-4-2-8-5-8-10v-6z"/><path d="M20 16a3.5 3.5 0 1 0 0 4"/></svg>
    <h3>COPYRIGHT PROTECTION</h3>
    <p>You own your content. Take it<br>down whenever you want</p>
  </div>
  <div class="feature" style="left:484px">
    <svg width="34" height="34" viewBox="0 0 34 34" fill="none" stroke="#fff" stroke-width="1.3"><rect x="3" y="4" width="28" height="18" rx="2"/><path d="M8 9h6M8 13h6M20 9h6M20 13h6M8 17h18"/><path d="M16 32v-9a2 2 0 0 1 4 0v5l4 1v3"/></svg>
    <h3>CUSTOMIZABLE SUBSCRIPTIONS</h3>
    <p>Build your own subscription<br>plan to fit your busines</p>
  </div>
</section>

<section class="abs fees">
  <svg class="abs" style="left:0;top:0" width="327" height="159" viewBox="0 0 327 159"><polygon points="198,0 327,0 327,159 133,159" fill="#c2a7ee"/><line x1="198" y1="0" x2="133" y2="159" stroke="#fff" stroke-width="3"/></svg>
  <div class="abs fees-label" style="left:25px;top:12px">COMPETITOR FEES</div>
  <div class="rival" style="top:50px"><i style="background:#f96d3a"></i>Brindlefold</div><div class="rate" style="top:47px">20 %</div>
  <div class="rival" style="top:94px"><i style="background:#2a9ee8"></i>Tovarenel</div><div class="rate" style="top:91px">42.5 %</div>
  <div class="rival" style="top:134px"><i style="background:#f0b23c"></i>Gleamwick</div><div class="rate" style="top:131px">25-35 %</div>
  <div class="our fees-label" style="top:13px">OUR FEES</div>
  <div class="our" style="top:56px;font-size:29px;font-weight:600">10%</div>
  <a class="abs btn btn-primary" style="left:197px;top:126px;width:101px;height:22px">GET STARTED</a>
</section>

<h3 class="abs signup-title">Create Your FREE Account</h3>
<form class="abs signup">
  <div class="field" style="top:9px">Username</div>
  <div class="field" style="top:33px">Email</div>
  <div class="field" style="top:57px">Password</div>
  <div class="field" style="top:81px">Repeat Password</div>
  <a class="abs btn btn-primary" style="left:18px;top:106px;width:100px;height:20px;border-radius:10px">REGISTER</a>
</form>

<footer class="abs footer">Copyright © 2020 LUMORABEY. Privacy Policy.</footer>

</body>
</html>
```